Pim Loft needs to tell the world it has new hours! *

Pim Loft is a cafe that has just changed it's hours of operation and added two happy hours during the week. We need to get the word out to the neighborhood that we are open earlier and that there is an awesome breakfast deal first thing in the morning.

I really love world war two propaganda poster design and am looking for a poster that follows those design traits. Once the design is accepted I will have a local print maker silkscreen the poster which will be posted widely in public places.

The information we want to disseminate is:
Pim Loft is now open at 7am on weekdays and 8am on weekends.

Weekdays we offer a happy hour from 7am - 8am. I really want to emphasize the morning opening hours during the week and happy hours to get people motivated to come in.

I was thinking about a poster perhaps with a bird pulling a worm from the ground or something like that. Early bird gets the worm kinda thing.

Pim Loft now open 7am Monday thru Friday with a "lil' breakfast" happy hour from 7am - 8am

Second happy hour 4pm - 6pm.

I need posters for the streets and a matching graphic for the website.

Target Market(s)

Local clientele that work and live in the neighborhood where the cafe is located

Industry/Entity Type

Cafe

Font styles to use
Serif
Sans Serif

Colors

Designer to choose colors to be used in the design.

Requirements
Must have
• Image of a one eared rabbit. This is our icon.
• Hours of new operation.
• Hours of happy hours.
• Horizontal orientation.
• 3 - 4 color design ready for color separation for printing.

```html
<!DOCTYPE html>
<html lang="en">
<head>
<meta charset="utf-8">
<title>Pim Loft — New Hours</title>
<link href="https://fonts.googleapis.com/css2?family=Crimson+Pro:wght@400;700&family=Kalam:wght@700&display=swap" rel="stylesheet">
<style>
  :root {
    --backdrop: #d9d9d9;
    --paper: #e9b886;
    --paper-light: #f1cf9f;
    --paper-edge: #e39a62;
    --ink: #231d1a;
    --band: #6fdcfb;
    --band-light: #8fe6fd;
    --bird-white: #f6f1e8;
    --bird-shade: #d9c2a0;
    --bird-line: #5a2a1c;
  }
  * { box-sizing: border-box; margin: 0; padding: 0; }
  html, body { width: 1200px; height: 1200px; overflow: hidden; }
  body {
    background: var(--backdrop);
    font-family: "Crimson Pro", Georgia, serif;
    color: var(--ink);
  }
  .poster {
    position: absolute;
    left: 187px; top: 20px;
    width: 826px; height: 1160px;
    background:
      radial-gradient(ellipse at 50% 55%, var(--paper-light) 0%, var(--paper) 55%, var(--paper-edge) 100%);
    overflow: hidden;
  }
  .center { position: absolute; left: 0; width: 100%; text-align: center; }
  .brand-mark {
    top: 70px;
    display: flex; justify-content: center; align-items: center; gap: 12px;
    font-size: 40px; font-weight: 700;
  }
  .brand-mark .dot { width: 22px; height: 22px; border-radius: 50%; background: var(--ink); }
  .headline {
    top: 180px;
    font-family: "Kalam", "Comic Sans MS", cursive;
    font-size: 72px; line-height: 1;
  }
  .hours-box {
    position: absolute; left: 67px; top: 276px; width: 692px; height: 59px;
    border: 1.5px solid var(--ink);
    display: flex; align-items: center; justify-content: center;
    font-size: 32px; font-weight: 700;
  }
  .intro { top: 344px; font-size: 29px; line-height: 33px; }
  .intro b { font-weight: 700; }
  .morning-hour { top: 416px; font-size: 44px; font-weight: 700; }
  .second-box {
    position: absolute; left: 208px; top: 483px; width: 409px; height: 50px;
    border: 1.5px solid var(--ink);
    display: flex; align-items: center; justify-content: center;
    font-size: 29px;
  }
  .second-box b { margin-left: 7px; }
  .illustration {
    position: absolute; left: 100px; top: 578px; width: 716px; height: 331px;
    border-radius: 10px 10px 0 0;
    border-bottom: 3px solid var(--bird-line);
    background: linear-gradient(160deg, var(--bird-white) 0%, var(--bird-shade) 100%);
  }
  .footer-band {
    position: absolute; left: 0; top: 909px; width: 100%; height: 251px;
    background: linear-gradient(180deg, var(--band) 0%, var(--band-light) 100%);
  }
  .pin { position: absolute; left: 399px; top: 930px; }
  .footer-name { top: 968px; font-size: 46px; font-weight: 700; }
  .address { top: 1040px; font-size: 27px; font-weight: 700; }
  .contacts {
    position: absolute; top: 1100px; left: 0; width: 100%;
    display: flex; justify-content: center; gap: 60px;
    font-size: 15px;
  }
  .contacts span { display: flex; align-items: center; gap: 7px; }
  .contacts .phone { font-size: 18px; }
  .contacts svg { flex: none; }
</style>
</head>
<body>
  <main class="poster">
    <div class="center brand-mark"><span class="dot"></span>Pim Loft</div>

    <h1 class="center headline">Pim Loft is now open</h1>

    <div class="hours-box">At 7am on weekdays &amp; 8am on weekends</div>

    <p class="center intro">Pim Loft now open 7am <b>Monday</b> thru <b>Friday</b><br>with a lil' breakfast <b>happy hour</b> from</p>

    <p class="center morning-hour">7am - 8am</p>

    <div class="second-box">Second happy hour <b>4pm - 6pm</b></div>

    <div class="illustration" role="img" aria-label="Hand-drawn white bird standing on the ground, pulling a long worm from the soil"></div>

    <section class="footer-band"></section>

    <svg class="pin" width="28" height="34" viewBox="0 0 28 34" aria-hidden="true">
      <path d="M14 1C7 1 2 6 2 13c0 9 12 20 12 20s12-11 12-20C26 6 21 1 14 1z" fill="var(--ink)"/>
      <circle cx="14" cy="13" r="4.5" fill="var(--band)"/>
    </svg>
    <p class="center footer-name">Pim Loft</p>
    <p class="center address">214 E Alder St, Seattle, WA 98102</p>

    <div class="contacts">
      <span class="phone">
        <svg width="16" height="16" viewBox="0 0 16 16" aria-hidden="true"><circle cx="8" cy="8" r="8" fill="var(--ink)"/><path d="M5 4.5c.5-.5 1-.4 1.3 0l.8 1.3c.2.4 0 .8-.3 1l-.4.3c.4 1 1.2 1.8 2.2 2.2l.3-.4c.3-.3.7-.5 1-.3l1.3.8c.4.3.5.8 0 1.3-.8.8-2 .9-3.4.1C6.2 9.8 5 8.4 4.6 7c-.3-1-.2-1.9.4-2.5z" fill="var(--band)"/></svg>
        (206) 555-0148
      </span>
      <span>
        <svg width="16" height="16" viewBox="0 0 16 16" aria-hidden="true"><circle cx="8" cy="8" r="8" fill="var(--ink)"/><rect x="4" y="5.5" width="8" height="5.5" fill="var(--band)"/><path d="M4 5.5l4 3 4-3" stroke="var(--ink)" stroke-width="1" fill="none"/></svg>
        info@pimloftcafe.com
      </span>
      <span>
        <svg width="16" height="16" viewBox="0 0 16 16" aria-hidden="true"><circle cx="8" cy="8" r="8" fill="var(--ink)"/><circle cx="8" cy="8" r="4.5" stroke="var(--band)" stroke-width="1" fill="none"/><path d="M3.5 8h9M8 3.5c-2 2.5-2 6.5 0 9M8 3.5c2 2.5 2 6.5 0 9" stroke="var(--band)" stroke-width="1" fill="none"/></svg>
        www.pimloftcafe.com
      </span>
    </div>
  </main>
</body>
</html>
```